Email Preference Page Design

We are looking for a 2 page design for our users to edit their email preferences and submit friend referrals. You can find the fuctionality, content and text here:

https://brightcart.examplemail.net/app/linkClick/7281/5c9a1b3e8d04f2aa/20583941/7f3d9e2b1a6c4058

* the shipping and billing address might be different so you need to show the billing if the "same as shipping" box is not checked. It can auto-hide like the page above shows if that fits your design.

* when the "unsubscribe from all email lists" box is selected, all the other checkbox options will hide as in the example page. We need you to show us what the site will look like with and without that checkbox selected.

We want to match these two pages to the general feel of these website pages:

www.brightcart.com
and
free.brightcart.com

The page should be very clean and tight. Project is for design only but must be able to be implemented in html showing button and checkbox states. Technically this must be two pages for our system - one for all the user info and one for individual email referrals (see example above).

Target Market(s)

video professionals

Industry/Entity Type

Shipping

Requirements
Must have
• our logo (see numerous versions attached)
well designed header
well designed sections
clean editable text
tight layout
html friendly
easy to understand
2 pages
Nice to have
• custom checkboxes and radio buttons

```html
<!DOCTYPE html>
<html lang="en">
<head>
<meta charset="utf-8">
<title>brightcart — Communication Preferences</title>
<link href="https://fonts.googleapis.com/css2?family=Source+Sans+3:wght@300;400;600;700&display=swap" rel="stylesheet">
<style>
  :root {
    --orange: #f26a1b;
    --orange-dark: #d9530c;
    --ink: #4a4a4a;
    --ink-soft: #6b6b6b;
    --line: #c9c9c9;
    --footer: #5b5b5b;
    --white: #ffffff;
  }
  * { box-sizing: border-box; margin: 0; padding: 0; }
  html, body { width: 1126px; height: 1200px; overflow: hidden; background: var(--white); }
  body { position: relative; font-family: "Source Sans 3", sans-serif; color: var(--ink); }

  .site-header { position: absolute; left: 0; top: 0; width: 1126px; height: 67px; }
  .brand { position: absolute; left: 169px; top: 14px; display: flex; align-items: center; gap: 10px; }
  .brand-dot { width: 22px; height: 22px; border-radius: 50%; background: var(--orange); }
  .brand-name { font-size: 34px; font-weight: 400; color: #2f2f2f; letter-spacing: 0.5px; line-height: 1; }

  .hero { position: absolute; left: 0; top: 67px; width: 1126px; height: 390px;
    background: radial-gradient(ellipse at 55% 40%, #9a9a9a 0%, #4b4b4b 40%, #1a1a1a 80%); }
  .hero-art { position: absolute; inset: 0; }
  .hero-brand { position: absolute; left: 0; right: 0; top: 220px; text-align: center;
    font-size: 30px; font-weight: 400; color: var(--white); }
  .hero-title { position: absolute; left: 0; right: 0; top: 280px; text-align: center;
    font-size: 27px; font-weight: 600; line-height: 35px; color: var(--white); }
  .hero-arrow { position: absolute; top: 173px; width: 46px; height: 46px; }

  .page-title { position: absolute; left: 0; right: 0; top: 482px; text-align: center;
    font-size: 34px; font-weight: 400; color: #555; }

  .section-heading { position: absolute; font-size: 19px; font-weight: 400; color: var(--orange); }
  .field { position: absolute; left: 169px; width: 227px; height: 24px; border: 1px solid var(--line);
    font-size: 10px; color: var(--ink-soft); padding: 0 8px; line-height: 22px; }
  .field-plus { position: absolute; left: 323px; font-size: 11px; color: var(--ink-soft); }

  .check-item { position: absolute; display: flex; align-items: flex-start; gap: 8px;
    font-size: 10px; color: var(--ink-soft); line-height: 16px; }
  .check-box { flex: none; width: 11px; height: 11px; border: 1px solid #bdbdbd; margin-top: 2px; background: var(--white); }
  .check-item.is-alert { font-weight: 700; color: var(--orange); font-size: 11px; }

  .lead { position: absolute; left: 428px; width: 530px; top: 557px; text-align: center;
    font-size: 19px; line-height: 24px; color: var(--orange); }
  .photo { position: absolute; top: 627px; width: 253px; height: 120px; }
  .photo-email { left: 428px; background: linear-gradient(180deg, #c7cdd1 0%, #7d878d 100%); }
  .photo-lasers { left: 703px; background: linear-gradient(135deg, #0b1440 0%, #0f5f6a 50%, #3a1a4a 100%); }
  .sub-heading { position: absolute; top: 764px; font-size: 14px; color: var(--orange); }

  .submit-button { position: absolute; left: 716px; top: 1045px; width: 232px; height: 56px;
    border: 1px solid var(--orange-dark); border-radius: 3px;
    background: linear-gradient(180deg, #f6822f 0%, var(--orange-dark) 100%);
    color: var(--white); font-family: inherit; font-size: 27px; font-weight: 700; text-align: center; line-height: 54px; }

  .site-footer { position: absolute; left: 0; top: 1138px; width: 1126px; height: 62px; background: var(--footer);
    color: var(--white); font-size: 7.5px; font-weight: 600; text-transform: uppercase; }
  .footer-links { position: absolute; left: 174px; top: 27px; display: flex; gap: 13px; }
  .follow { position: absolute; left: 794px; top: 18px; display: flex; align-items: center; gap: 4px; }
  .follow-label { margin-right: 2px; }
  .social { width: 25px; height: 25px; border-radius: 50%; background: #7a8598; }
</style>
</head>
<body>
  <header class="site-header">
    <div class="brand"><span class="brand-dot"></span><span class="brand-name">brightcart</span></div>
  </header>

  <section class="hero">
    <div class="hero-art" role="img" aria-label="Black and white night photograph of a city skyline and a lit suspension bridge over the river"></div>
    <svg class="hero-arrow" style="left:77px" viewBox="0 0 46 46"><circle cx="23" cy="23" r="21" fill="none" stroke="rgba(255,255,255,.35)" stroke-width="2"/><path d="M27 14 L18 23 L27 32" fill="none" stroke="rgba(255,255,255,.35)" stroke-width="3"/></svg>
    <svg class="hero-arrow" style="left:995px" viewBox="0 0 46 46"><circle cx="23" cy="23" r="21" fill="none" stroke="rgba(255,255,255,.35)" stroke-width="2"/><path d="M19 14 L28 23 L19 32" fill="none" stroke="rgba(255,255,255,.35)" stroke-width="3"/></svg>
    <div class="hero-brand">brightcart</div>
    <h1 class="hero-title">Help us filter our emails so we are only sending<br>relevant information to you.</h1>
  </section>

  <h2 class="page-title">Communication Preferences</h2>

  <h3 class="section-heading" style="left:168px;top:556px">Contact Info</h3>
  <div class="field" style="top:593px">First Name</div>
  <div class="field" style="top:626px">Last Name</div>
  <div class="field" style="top:657px">Email</div>
  <div class="field" style="top:690px">Phone 1</div>
  <div class="field" style="top:721px">Address 1</div>
  <div class="field" style="top:754px">Address 2</div>
  <div class="field" style="top:786px">Address 3</div>
  <div class="field" style="top:819px">City</div>
  <div class="field" style="top:850px">Country</div>
  <div class="field" style="top:883px">State</div>
  <div class="field" style="top:915px;width:146px">Postal Code + 4</div>
  <span class="field-plus" style="top:920px">+</span>
  <div class="field" style="top:915px;left:338px;width:58px"></div>

  <h3 class="section-heading" style="left:168px;top:952px;font-size:15px">Shipping Address</h3>
  <label class="check-item" style="left:169px;top:982px;width:232px"><span class="check-box"></span>Billing address is same as shipping address</label>
  <label class="check-item" style="left:169px;top:1004px;width:232px"><span class="check-box"></span>Subscribe me to your general email list&nbsp; This monthly email includes free video loops and VIP sale notices</label>

  <p class="lead">Help us filter our emails so we are only sending<br>relevant information to you.</p>
  <div class="photo photo-email" role="img" aria-label="Illustration of a hand touching an envelope with an email symbol"></div>
  <div class="photo photo-lasers" role="img" aria-label="Photograph of green and blue laser beams over a concert crowd"></div>

  <h4 class="sub-heading" style="left:427px">Send me emails about these product types:</h4>
  <label class="check-item" style="left:429px;top:794px"><span class="check-box"></span>Low energy motion loops</label>
  <label class="check-item" style="left:429px;top:818px"><span class="check-box"></span>High energy motion loops</label>
  <label class="check-item" style="left:429px;top:842px"><span class="check-box"></span>Timelapse footage</label>
  <label class="check-item" style="left:429px;top:866px"><span class="check-box"></span>Worship or wedding motion loops</label>
  <label class="check-item" style="left:429px;top:890px"><span class="check-box"></span>Pre-mixed DVDs and BluRay</label>
  <label class="check-item" style="left:429px;top:914px"><span class="check-box"></span>Entertainment lasers for concerts and clubs</label>
  <label class="check-item" style="left:429px;top:938px"><span class="check-box"></span>Entertainment lasers for text &amp; logo display</label>
  <label class="check-item" style="left:429px;top:962px"><span class="check-box"></span>Custom logo animation services</label>
  <label class="check-item" style="left:429px;top:986px"><span class="check-box"></span>Video software for creating video animations</label>
  <label class="check-item" style="left:429px;top:1010px"><span class="check-box"></span>Video software for live performance (Vjing)</label>

  <h4 class="sub-heading" style="left:703px">I am Involved in or have interest in:</h4>
  <label class="check-item" style="left:705px;top:794px"><span class="check-box"></span>VJing (live performance video)</label>
  <label class="check-item" style="left:705px;top:818px"><span class="check-box"></span>DJing (live performance audio+video)</label>
  <label class="check-item" style="left:705px;top:842px"><span class="check-box"></span>Performing in a band</label>
  <label class="check-item" style="left:705px;top:866px"><span class="check-box"></span>Video editing</label>
  <label class="check-item" style="left:705px;top:890px"><span class="check-box"></span>Corporate presentations</label>
  <label class="check-item" style="left:705px;top:914px"><span class="check-box"></span>Worship video services</label>
  <label class="check-item" style="left:705px;top:938px"><span class="check-box"></span>Lasers for entertainment &amp; branding</label>
  <label class="check-item" style="left:705px;top:962px"><span class="check-box"></span>Special offers from BrightCart partners</label>
  <label class="check-item is-alert" style="left:705px;top:987px"><span class="check-box"></span>Unsubscribe from all email lists</label>

  <button class="submit-button" type="submit">Submit Now</button>

  <footer class="site-footer">
    <nav class="footer-links">
      <span>Copyright © 2013. Halvane all rights reserved.</span>
      <span>Terms &amp; Conditions</span><span>|</span>
      <span>Privacy Policy</span><span>|</span>
      <span>Disclaimer</span>
    </nav>
    <div class="follow">
      <span class="follow-label">Follow us :</span>
      <span class="social" aria-label="Social link"></span>
      <span class="social" aria-label="Social link"></span>
      <span class="social" aria-label="Social link"></span>
      <span class="social" aria-label="Social link"></span>
    </div>
  </footer>
</body>
</html>
```